Corwell's Heating needs SUV Wrap design

We are looking for options for an SUV wrap, we currently have a van wrap which we would like to play off to design the SUV wrap. We would like to see designs that use our logo as well as our van wrap to stay branded.

Colors; Navy blue & grey as in logo
Design - Minimal design - not full truck. 1/2 of back - no design on front end
Please see our current warps to match style.

I have attached full ZIP file of logo

Industry/Entity Type

HVAC

Font styles to use
Serif
Sans Serif

Colors
0054AA
0677BA
7BADD7
CADEEF
E8F1F8

Requirements
Must have
• Minimalist wrap design - Must have name of company and logo. Colors: Blue and Navy
Should not have
• Full wrap, other colors and fonts that don't match our current design

```html
<!DOCTYPE html>
<html lang="en">
<head>
<meta charset="utf-8">
<title>Corwell's Heating – SUV Wrap</title>
<link href="https://fonts.googleapis.com/css2?family=Arimo:wght@400;700&family=Libre+Baskerville:wght@700&display=swap" rel="stylesheet">
<style>
  :root {
    --navy: #0d3a93;
    --blue: #1f4fb0;
    --grey: #8e949b;
    --grey-light: #c9cdd2;
    --body: #f2f3f4;
    --glass: #2b2f36;
    --tyre: #3a3d42;
    --rim: #b9bdc2;
    --hub: #8e949b;
    --page: #e9ecef;
    --white: #ffffff;
    --phone: #6b7076;
  }
  html, body {
    margin: 0;
    width: 1200px;
    height: 667px;
    overflow: hidden;
    background: var(--page);
  }
  .wrap-sheet { display: block; width: 1200px; height: 667px; }
  .side-view { display: block; width: 1200px; height: 333px; }
  .body-shell { fill: var(--body); stroke: var(--grey-light); stroke-width: 1.5; }
  .glass { fill: var(--glass); }
  .band-navy { fill: var(--blue); }
  .band-grey { fill: var(--grey); }
  .band-sheen { fill: var(--grey-light); opacity: .55; }
  .tyre { fill: var(--tyre); }
  .rim { fill: var(--rim); }
  .hub { fill: var(--hub); }
  .brand-dot { fill: var(--navy); }
  .brand-name { font-family: "Libre Baskerville", serif; font-weight: 700; font-size: 28px; fill: var(--navy); }
  .tagline { font-family: "Arimo", sans-serif; font-weight: 700; font-size: 10.5px; fill: var(--navy); }
  .phone { font-family: "Arimo", sans-serif; font-weight: 700; font-size: 18px; fill: var(--phone); letter-spacing: .5px; }
  .web { font-family: "Arimo", sans-serif; font-weight: 700; font-size: 10px; fill: var(--navy); }
  .badge-ring { fill: none; stroke: var(--navy); stroke-width: 2; }
  .badge-num { font-family: "Arimo", sans-serif; font-weight: 700; font-size: 10px; fill: var(--navy); }
  .badge-label { font-family: "Arimo", sans-serif; font-weight: 700; font-size: 6.5px; fill: var(--navy); }
  .service { font-family: "Arimo", sans-serif; font-weight: 700; font-size: 10.5px; fill: var(--white); }
</style>
</head>
<body>
<div class="wrap-sheet">

  <svg class="side-view side-passenger" viewBox="0 0 1200 333" xmlns="http://www.w3.org/2000/svg">
    <defs>
      <clipPath id="shell-clip-a">
        <path d="M250 250 L245 190 Q250 120 300 70 L330 50 Q340 45 360 45 L760 45 Q800 45 840 90 L900 140 Q960 150 990 175 L1000 230 L995 265 L940 268 A58 58 0 0 0 825 268 L455 268 A58 58 0 0 0 340 268 L262 268 Z"/>
      </clipPath>
    </defs>
    <g class="vehicle">
      <path class="body-shell" d="M250 250 L245 190 Q250 120 300 70 L330 50 Q340 45 360 45 L760 45 Q800 45 840 90 L900 140 Q960 150 990 175 L1000 230 L995 265 L940 268 A58 58 0 0 0 825 268 L455 268 A58 58 0 0 0 340 268 L262 268 Z"/>
      <g clip-path="url(#shell-clip-a)">
        <path class="band-sheen" d="M470 110 L560 110 L820 240 L720 240 Z"/>
        <path class="band-grey" d="M240 172 L480 178 L810 225 L810 240 L470 192 L240 188 Z"/>
        <path class="band-navy" d="M240 186 L470 190 L810 238 L820 275 L240 275 Z"/>
        <path class="band-navy" d="M290 62 L455 52 L430 108 L278 112 Z"/>
      </g>
      <path class="glass" d="M300 108 L335 60 L440 57 L420 104 Z"/>
      <path class="glass" d="M475 105 L500 58 L605 55 L610 120 Z"/>
      <path class="glass" d="M625 120 L620 55 L720 58 L795 125 Z"/>
      <circle class="tyre" cx="397" cy="272" r="50"/><circle class="rim" cx="397" cy="272" r="36"/><circle class="hub" cx="397" cy="272" r="8"/>
      <circle class="tyre" cx="882" cy="272" r="50"/><circle class="rim" cx="882" cy="272" r="36"/><circle class="hub" cx="882" cy="272" r="8"/>
    </g>

    <g class="contact-block">
      <circle class="badge-ring" cx="340" cy="125" r="12"/>
      <text class="badge-num" x="340" y="129" text-anchor="middle">24/7</text>
      <text class="badge-label" x="360" y="123">SERVICE</text>
      <text class="badge-label" x="356" y="133">AVAILABLE</text>
      <text class="phone" x="317" y="157">555 .014. 2260</text>
      <text class="web" x="323" y="171">www.CorwellsHeating.com</text>
    </g>

    <g class="brand-block">
      <circle class="brand-dot" cx="502" cy="186" r="24"/>
      <text class="tagline" x="790" y="162" text-anchor="end">Commercial &amp; Residential</text>
      <text class="brand-name" x="534" y="198">Corwell's Heating</text>
    </g>

    <g class="service-list">
      <text class="service" x="482" y="241">• Preventative Maintenance</text>
      <text class="service" x="482" y="254">• Sheet Metal Fabrication</text>
      <text class="service" x="634" y="245">• Installation</text>
      <text class="service" x="634" y="258">• Service</text>
      <text class="service" x="708" y="254">• Indoor Air Quality</text>
    </g>
  </svg>

  <svg class="side-view side-driver" viewBox="0 0 1200 333" xmlns="http://www.w3.org/2000/svg">
    <defs>
      <clipPath id="shell-clip-b">
        <path d="M250 250 L245 190 Q250 120 300 70 L330 50 Q340 45 360 45 L760 45 Q800 45 840 90 L900 140 Q960 150 990 175 L1000 230 L995 265 L940 268 A58 58 0 0 0 825 268 L455 268 A58 58 0 0 0 340 268 L262 268 Z"/>
      </clipPath>
    </defs>
    <g class="vehicle" transform="translate(1200 0) scale(-1 1)">
      <path class="body-shell" d="M250 250 L245 190 Q250 120 300 70 L330 50 Q340 45 360 45 L760 45 Q800 45 840 90 L900 140 Q960 150 990 175 L1000 230 L995 265 L940 268 A58 58 0 0 0 825 268 L455 268 A58 58 0 0 0 340 268 L262 268 Z"/>
      <g clip-path="url(#shell-clip-b)">
        <path class="band-sheen" d="M470 110 L560 110 L820 240 L720 240 Z"/>
        <path class="band-grey" d="M240 172 L480 178 L810 225 L810 240 L470 192 L240 188 Z"/>
        <path class="band-navy" d="M240 186 L470 190 L810 238 L820 275 L240 275 Z"/>
        <path class="band-navy" d="M290 62 L455 52 L430 108 L278 112 Z"/>
      </g>
      <path class="glass" d="M300 108 L335 60 L440 57 L420 104 Z"/>
      <path class="glass" d="M475 105 L500 58 L605 55 L610 120 Z"/>
      <path class="glass" d="M625 120 L620 55 L720 58 L795 125 Z"/>
      <circle class="tyre" cx="397" cy="272" r="50"/><circle class="rim" cx="397" cy="272" r="36"/><circle class="hub" cx="397" cy="272" r="8"/>
      <circle class="tyre" cx="882" cy="272" r="50"/><circle class="rim" cx="882" cy="272" r="36"/><circle class="hub" cx="882" cy="272" r="8"/>
    </g>

    <g class="contact-block">
      <circle class="badge-ring" cx="780" cy="125" r="12"/>
      <text class="badge-num" x="780" y="129" text-anchor="middle">24/7</text>
      <text class="badge-label" x="800" y="123">SERVICE</text>
      <text class="badge-label" x="796" y="133">AVAILABLE</text>
      <text class="phone" x="757" y="157">555 .014. 2260</text>
      <text class="web" x="763" y="171">www.CorwellsHeating.com</text>
    </g>

    <g class="brand-block">
      <text class="tagline" x="402" y="162">Commercial &amp; Residential</text>
      <text class="brand-name" x="402" y="198">Corwell's Heating</text>
      <circle class="brand-dot" cx="696" cy="186" r="24"/>
    </g>

    <g class="service-list">
      <text class="service" x="716" y="241" text-anchor="end">Preventative Maintenance •</text>
      <text class="service" x="716" y="254" text-anchor="end">Sheet Metal Fabrication •</text>
      <text class="service" x="566" y="245" text-anchor="end">Installation •</text>
      <text class="service" x="566" y="258" text-anchor="end">Service •</text>
      <text class="service" x="492" y="254" text-anchor="end">Indoor Air Quality •</text>
    </g>
  </svg>

</div>
</body>
</html>
```